Paloverde Coffee and Kitchen needs a food menu.

We need a menu design for a small coffeeshop in San Pedro Sula Honduras. We serve bistro style food. It should look clean, eye pleasing, modern and organic.
We are all about the home made feel. Superb quality, only natural ingredients, everything is made from scratch. We serve soups, sandwiches, salads, we specialize in desserts and gelato. We are located inside a hotel, we have both english and spanish speaking customers.

Target Market(s)

Young adults

Industry/Entity Type

Restaurant

Contact Information for Business Card

Paloverde
info@paloverdemx.example
Hotel Brisa Lodge Plaza, San Pedro Sula Honduras
+50427408263

Font styles to use
Sans Serif

Colors

Designer to choose colors to be used in the design.

Requirements
Must have
• elegant and clean feel.
Nice to have
• lettering.

```html
<!DOCTYPE html>
<html lang="es">
<head>
<meta charset="utf-8">
<title>Paloverde — Menú</title>
<link href="https://fonts.googleapis.com/css2?family=Oxygen:wght@300;400;700&display=swap" rel="stylesheet">
<style>
  :root {
    --red: #d2232a;
    --ink: #1a1a1a;
    --paper: #ffffff;
  }
  * { box-sizing: border-box; margin: 0; padding: 0; }
  html, body { width: 1200px; height: 849px; overflow: hidden; background: var(--paper); }
  body { font-family: "Oxygen", Arial, sans-serif; color: var(--ink); }
  .menu { position: relative; width: 1200px; height: 849px; }

  .section-title { position: absolute; color: var(--red); font-weight: 700; font-size: 31px; letter-spacing: 0.2px; line-height: 1; background: var(--paper); padding: 0 8px 0 0; }
  .section-sub { position: absolute; font-size: 11px; font-style: italic; font-weight: 700; }

  .frame { position: absolute; border: 2px dotted var(--red); border-radius: 22px; }

  .item { position: absolute; }
  .item-name { font-size: 13px; font-weight: 700; letter-spacing: 0.4px; text-transform: uppercase; }
  .item-price { position: absolute; top: 0; right: 0; font-size: 13px; }
  .item-en { font-size: 11px; font-style: italic; font-weight: 700; margin-top: 1px; }
  .item-desc { font-size: 11.5px; margin-top: 6px; line-height: 1.3; }
  .item-desc em { display: block; font-style: italic; }

  .row { position: absolute; font-size: 14px; display: flex; justify-content: space-between; }
  .row.small { font-size: 11.5px; font-weight: 700; }

  .band { position: absolute; left: 0; top: 270px; }

  .brand { position: absolute; left: 1100px; top: 782px; display: flex; align-items: center; gap: 5px; color: var(--ink); font-size: 14px; font-weight: 400; }
  .brand-dot { width: 8px; height: 8px; border-radius: 50%; background: var(--ink); }
</style>
</head>
<body>
<main class="menu">

  <!-- Desserts -->
  <h2 class="section-title" style="left:36px;top:42px;">PALOVERDE</h2>
  <p class="section-sub" style="left:36px;top:72px;">desserts</p>

  <div class="item" style="left:36px;top:120px;width:236px;">
    <p class="item-name">Yougurt Brulle</p><span class="item-price">9.9</span>
    <p class="item-en">yougurt brulle</p>
    <p class="item-desc">explanation of ingredient in Spanish<em>explanation of ingredient in English</em></p>
  </div>
  <div class="item" style="left:36px;top:204px;width:236px;">
    <p class="item-name">Yougurt Brulle</p><span class="item-price">9.9</span>
    <p class="item-en">yougurt brulle</p>
    <p class="item-desc">explanation of ingredient in Spanish<em>explanation of ingredient in English</em></p>
  </div>
  <div class="item" style="left:36px;top:287px;width:236px;">
    <p class="item-name">Yougurt Brulle</p><span class="item-price">9.9</span>
    <p class="item-en">yougurt brulle</p>
    <p class="item-desc">explanation of ingredient in Spanish<em>explanation of ingredient in English</em></p>
  </div>

  <!-- Wine & liqueurs -->
  <div class="frame" style="left:302px;top:56px;width:520px;height:200px;"></div>
  <h2 class="section-title" style="left:316px;top:38px;padding:0 12px 0 4px;">WINE &amp; LIQUEURS</h2>
  <p class="section-sub" style="left:319px;top:69px;font-weight:400;">wine &amp; liquors</p>

  <div class="row" style="left:318px;top:116px;width:200px;"><span>RED WINE</span><span>9.9</span></div>
  <div class="row" style="left:318px;top:150px;width:200px;"><span>WHITE WINE</span><span>9.9</span></div>
  <div class="row" style="left:318px;top:182px;width:200px;"><span>MARTINI</span><span>9.9</span></div>
  <div class="row" style="left:318px;top:213px;width:200px;"><span>MOJITO</span><span>9.9</span></div>
  <div class="row" style="left:600px;top:116px;width:200px;"><span>BEER</span><span>9.9</span></div>
  <div class="row" style="left:600px;top:150px;width:200px;"><span>WHITE WINE</span><span>9.9</span></div>
  <div class="row" style="left:600px;top:182px;width:200px;"><span>MARTINI</span><span>9.9</span></div>
  <div class="row" style="left:600px;top:213px;width:200px;"><span>MOJITO</span><span>9.9</span></div>

  <!-- Coffee & tea -->
  <div class="frame" style="left:854px;top:56px;width:279px;height:246px;"></div>
  <h2 class="section-title" style="left:882px;top:40px;padding:0 12px 0 6px;">CAFÉ &amp; TÉ</h2>
  <p class="section-sub" style="left:888px;top:72px;font-weight:400;">coffee</p>

  <div class="row small" style="left:888px;top:119px;width:158px;"><span>ESPRESSO</span><span>9.9</span></div>
  <div class="row small" style="left:888px;top:148px;width:158px;"><span>ESPRESSO</span><span>9.9</span></div>
  <div class="row small" style="left:888px;top:177px;width:158px;"><span>ESPRESSO</span><span>9.9</span></div>
  <div class="row small" style="left:888px;top:206px;width:158px;"><span>ESPRESSO</span><span>9.9</span></div>
  <div class="row small" style="left:888px;top:235px;width:158px;"><span>ESPRESSO</span><span>9.9</span></div>
  <div class="row small" style="left:888px;top:264px;width:158px;"><span>MATCHA</span><span>9.9</span></div>

  <!-- Photo band -->
  <svg class="band" width="1200" height="330" viewBox="0 270 1200 330" aria-hidden="false">
    <defs>
      <linearGradient id="g-pudding" x1="0" y1="0" x2="0" y2="1"><stop offset="0" stop-color="#efe6d2"/><stop offset="1" stop-color="#d9c9a6"/></linearGradient>
      <linearGradient id="g-mango" x1="0" y1="0" x2="0" y2="1"><stop offset="0" stop-color="#f0d27a"/><stop offset="1" stop-color="#c89a3c"/></linearGradient>
      <linearGradient id="g-macaron" x1="0" y1="0" x2="1" y2="1"><stop offset="0" stop-color="#f1ece6"/><stop offset="1" stop-color="#cfc4b9"/></linearGradient>
      <linearGradient id="g-cake" x1="0" y1="0" x2="1" y2="1"><stop offset="0" stop-color="#e9e4dc"/><stop offset="1" stop-color="#8f8a84"/></linearGradient>
      <linearGradient id="g-wine" x1="0" y1="0" x2="0" y2="1"><stop offset="0" stop-color="#8b6a4a"/><stop offset="1" stop-color="#3d1c18"/></linearGradient>
      <linearGradient id="g-beer" x1="0" y1="0" x2="0" y2="1"><stop offset="0" stop-color="#c9c3b2"/><stop offset="1" stop-color="#6b6448"/></linearGradient>
      <linearGradient id="g-latte" x1="0" y1="0" x2="0" y2="1"><stop offset="0" stop-color="#d8b58a"/><stop offset="1" stop-color="#a97c4e"/></linearGradient>
      <linearGradient id="g-burger" x1="0" y1="0" x2="0" y2="1"><stop offset="0" stop-color="#b98a55"/><stop offset="1" stop-color="#5e4a2c"/></linearGradient>
    </defs>
    <polygon role="img" aria-label="Photo: creamy dessert cup with spoon" fill="url(#g-pudding)" points="0,434 149,396 149,472"/>
    <polygon role="img" aria-label="Photo: mango gelato in a glass bowl" fill="url(#g-mango)" points="174,389 308,355 308,513 174,479"/>
    <polygon role="img" aria-label="Photo: stacked macarons" fill="url(#g-macaron)" points="333,349 454,318 454,550 333,519"/>
    <polygon role="img" aria-label="Photo: cookies and cream cheesecake" fill="url(#g-cake)" points="478,312 588,283 588,585 478,556"/>
    <polygon role="img" aria-label="Photo: wine bottles and a glass of red wine" fill="url(#g-wine)" points="612,283 720,311 720,557 612,585"/>
    <polygon role="img" aria-label="Photo: bottled beers on a table" fill="url(#g-beer)" points="746,318 868,349 868,519 746,550"/>
    <polygon role="img" aria-label="Photo: latte with foam art" fill="url(#g-latte)" points="892,355 1026,389 1026,479 892,513"/>
    <polygon role="img" aria-label="Photo: burger with greens" fill="url(#g-burger)" points="1050,396 1200,434 1050,472"/>
    <g fill="none" stroke="#d2232a" stroke-width="2" stroke-dasharray="0 6" stroke-linecap="round">
      <line x1="30" y1="418" x2="496" y2="288"/>
      <line x1="704" y1="286" x2="1172" y2="418"/>
      <line x1="30" y1="450" x2="300" y2="526"/>
      <line x1="704" y1="580" x2="1172" y2="450"/>
    </g>
  </svg>

  <!-- Gelato & sorbets -->
  <div class="frame" style="left:26px;top:598px;width:552px;height:226px;"></div>
  <h2 class="section-title" style="left:36px;top:580px;padding:0 12px 0 2px;">GELATO &amp; SORBETS</h2>
  <p class="section-sub" style="left:37px;top:612px;font-weight:400;">gelato &amp; sorbets</p>

  <div class="item" style="left:37px;top:660px;width:237px;">
    <p class="item-name">Gelato Vegano</p><span class="item-price">9.9</span>
    <p class="item-en">gelato vegano</p>
    <p class="item-desc">explanation of ingredient in Spanish<em>explanation of ingredient in English</em></p>
  </div>
  <div class="item" style="left:37px;top:743px;width:237px;">
    <p class="item-name">Gelato Vegano</p><span class="item-price">9.9</span>
    <p class="item-en">gelato vegano</p>
    <p class="item-desc">explanation of ingredient in Spanish<em>explanation of ingredient in English</em></p>
  </div>
  <div class="item" style="left:319px;top:661px;width:237px;">
    <p class="item-name">Gelato Vegano</p><span class="item-price">9.9</span>
    <p class="item-en">gelato vegano</p>
    <p class="item-desc">explanation of ingredient in Spanish<em>explanation of ingredient in English</em></p>
  </div>
  <div class="item" style="left:319px;top:744px;width:237px;">
    <p class="item-name">Gelato Vegano</p><span class="item-price">9.9</span>
    <p class="item-en">gelato vegano</p>
    <p class="item-desc">explanation of ingredient in Spanish<em>explanation of ingredient in English</em></p>
  </div>

  <!-- Other -->
  <h2 class="section-title" style="left:600px;top:602px;">OTRO</h2>
  <p class="section-sub" style="left:600px;top:634px;font-weight:400;">other</p>

  <div class="item" style="left:600px;top:666px;width:236px;">
    <p class="item-name">Hamburguesa</p><span class="item-price">9.9</span>
    <p class="item-en">burger</p>
    <p class="item-desc">explanation of ingredient in Spanish<em>explanation of ingredient in English</em></p>
  </div>
  <div class="item" style="left:600px;top:747px;width:236px;">
    <p class="item-name">Hamburguesa</p><span class="item-price">9.9</span>
    <p class="item-en">burger</p>
    <p class="item-desc">explanation of ingredient in Spanish<em>explanation of ingredient in English</em></p>
  </div>
  <div class="item" style="left:888px;top:563px;width:236px;">
    <p class="item-name">Hamburguesa</p><span class="item-price">9.9</span>
    <p class="item-en">burger</p>
    <p class="item-desc">explanation of ingredient in Spanish<em>explanation of ingredient in English</em></p>
  </div>
  <div class="item" style="left:888px;top:644px;width:236px;">
    <p class="item-name">Hamburguesa</p><span class="item-price">9.9</span>
    <p class="item-en">burger</p>
    <p class="item-desc">explanation of ingredient in Spanish<em>explanation of ingredient in English</em></p>
  </div>
  <div class="item" style="left:888px;top:724px;width:236px;">
    <p class="item-name">Hamburguesa</p><span class="item-price">9.9</span>
    <p class="item-en">burger</p>
    <p class="item-desc">explanation of ingredient in Spanish<em>explanation of ingredient in English</em></p>
  </div>

  <!-- Brand -->
  <div class="brand"><span>paloverde</span><span class="brand-dot"></span></div>

</main>
</body>
</html>
```